Business Cards For Glintwell
Desmond Kuvetti
Simple
CEO and Founder
2871 Pellfield Ln Brockville Ontario K3P2c8
Desmond@Kuvetti-mail.test
Keep it simple and clean. We want the logo BIG on the one side and company info on the other. If you can get some type of interlock going from bad to restored too that might look nice faded as a background on one of the sides.
750PineRidgeRnR 750PineRidgeRnR
https://www.socialpage.test/750PineRidgeRR/photos/pb.382915067214433.-1109384000.1285719304./517293048116520/?type=3&theater this is a good picture that would be nice to have one one side of the cards faded out
Logo has been uploaded.
Grafto Grafto
kindly upload logo

```html
<!DOCTYPE html>
<html lang="en">
<head>
<meta charset="utf-8">
<title>Glintwell Business Cards</title>
<link rel="stylesheet" href="https://fonts.googleapis.com/css2?family=Oswald:wght@600&family=Open+Sans:ital,wght@0,400;0,600;1,400&display=swap">
<style>
  :root {
    --page: #e6e6e8;
    --card: #ffffff;
    --navy: #2a3377;
    --ink: #1f2230;
    --stripe-dark: #2b2b2e;
    --stripe-grey: #8e8f94;
    --muted: #5a5d70;
  }
  * { margin: 0; padding: 0; box-sizing: border-box; }
  html, body { width: 1200px; height: 951px; overflow: hidden; background: var(--page); }
  .canvas { position: relative; width: 1200px; height: 951px; }
  .card {
    position: absolute; left: 240px; width: 720px; height: 411px;
    background: var(--card); border-radius: 22px; overflow: hidden;
    box-shadow: 0 6px 18px rgba(0,0,0,0.12);
  }
  .card--front { top: 43px; }
  .card--back { top: 497px; }
  .brand-name {
    font-family: "Oswald", sans-serif; font-weight: 600;
    color: var(--navy); text-transform: uppercase; letter-spacing: 2px; line-height: 1;
  }
  .card--front .brand-name {
    position: absolute; left: 0; right: 0; top: 160px; text-align: center; font-size: 88px;
  }
  .card__wave { position: absolute; inset: 0; width: 720px; height: 411px; }
  .card--back .brand-name {
    position: absolute; right: 60px; top: 118px; font-size: 62px;
  }
  .contact-list {
    position: absolute; left: 34px; top: 150px; list-style: none;
    font-family: "Open Sans", sans-serif; font-size: 13px; color: #fff;
  }
  .contact-list li { display: flex; align-items: center; gap: 9px; height: 24px; }
  .contact-list .dot { width: 12px; height: 12px; border-radius: 50%; background: #fff; flex: none; }
  .holder {
    position: absolute; right: 60px; top: 300px; text-align: right;
    font-family: "Open Sans", sans-serif; color: var(--navy);
  }
  .holder__name { font-size: 22px; font-weight: 600; }
  .holder__title { font-size: 16px; font-style: italic; color: var(--muted); }
</style>
</head>
<body>
<main class="canvas">
  <section class="card card--front">
    <div class="brand-name">Glintwell</div>
  </section>

  <section class="card card--back">
    <svg class="card__wave" viewBox="0 0 720 411" aria-hidden="true">
      <path d="M0,95 C120,45 210,40 270,150 S340,360 390,411 L0,411 Z" fill="var(--navy)"/>
      <path d="M0,70 C130,15 230,20 290,135 S365,355 415,411" fill="none" stroke="var(--stripe-grey)" stroke-width="14"/>
      <path d="M0,52 C135,-5 245,5 305,125 S382,350 435,411" fill="none" stroke="var(--stripe-dark)" stroke-width="7"/>
    </svg>
    <ul class="contact-list">
      <li><span class="dot"></span>2871 Pellfield Ln</li>
      <li><span class="dot"></span>Brockville ON K3P2c8</li>
      <li><span class="dot"></span>613 555 0142</li>
      <li><span class="dot"></span>613 555 0187</li>
      <li><span class="dot"></span>Desmond@Kuvetti-mail.test</li>
      <li><span class="dot"></span>www.glintwell.test</li>
    </ul>
    <div class="brand-name">Glintwell</div>
    <div class="holder">
      <div class="holder__name">Desmond Kuvetti</div>
      <div class="holder__title">Owner / C.E.O.</div>
    </div>
  </section>
</main>
</body>
</html>
```